Marisol Penhaw tutoring Advertising package - flyers, posters, business card and logo

I am looking for a flyer design for my tutoring business, it needs to explain what tutoring services I offer, how much I charge, why my services are worthwhile, it should include some photos of me and the tutoring centre,

It needs to include my phone number and my website. It should quote from some of the testimonials I have received from parents and children.

My website is www.marisolpenhaw.example My Facebook page can be found at https://www.facebook.example/marisolpenhawtutoring These pages include a range of photos and quotes that you can use.

I am not sure about the colours and designs that I would like, that's why I'm using Artflock!
I'm looking to appeal to parents inform them of my skills and experience.

I'm charging $45 for sessions of an hour and 15 minutes. 2 sessions per week will cost $80. I tutor Monday to Friday afternoons and evenings along with all day Saturdays. The assessment is free.

I tutor children from K-9 in English and Maths. I'm mainly aiming at parents whose children are struggling a little bit at school although I can help children who are doing well too.
I am highly skilled at helping children who can't read, I have a comprehensive program, the Calder program, that specifically teaches children the skills they need to read fluently and successfully.

Similarly I have had a lot of experience at helping children improve their Maths skills. I am well resourced with a wide range of hands on resources, paper resources and electronic resources.

Children will get better NAPLAN results if I tutor them (NAPLAN is the national series of tests in Australia).

I'm after a DL double sided flyer, and an A4 flyer. I'm also looking for two A2 posters and two A3 posters. Finally, I want a business card too. I don't have a logo for the business and I'd love to have one!

Target Market(s)

Parents of school aged children

Industry/Entity Type

Education

Colors

Designer to choose colors to be used in the design.

Requirements
Must have
• my name, my photo, length and cost of my sessions, email and phone contact details. Subjects and age ranges that I teach, times that I tutor. Website and/or Facebook page references. Quotes from Testimonials
Nice to have
• The A2 and A3 posters should complement each other.

```html
<!DOCTYPE html>
<html lang="en">
<head>
<meta charset="utf-8">
<title>Marisol Penhaw Tutoring – Flyer</title>
<link rel="stylesheet" href="https://fonts.googleapis.com/css2?family=Montserrat:wght@400;600;700;800&family=Raleway:wght@400;500;600&display=swap">
<style>
  :root{
    --navy:#0c4a6a;
    --navy-deep:#093a55;
    --sky:#3d9dc9;
    --blue:#1d6fa0;
    --ink:#1e2a33;
    --dot-red:#e06464;
    --paper:#ffffff;
    --paper-shade:#eef1f4;
  }
  *{box-sizing:border-box;margin:0;padding:0}
  html,body{width:950px;height:1200px;overflow:hidden;background:#f4f5f6}
  .flyer{position:relative;width:950px;height:1200px;overflow:hidden;
    background:linear-gradient(180deg,var(--paper) 0%,var(--paper) 60%,var(--paper-shade) 100%);
    font-family:"Raleway",sans-serif;color:var(--ink)}
  .hero-photo{position:absolute;left:0;top:0;width:600px;height:700px;
    background:
      radial-gradient(ellipse 180px 200px at 250px 480px,#f3d2bd 0%,rgba(243,210,189,0) 100%),
      radial-gradient(ellipse 230px 160px at 360px 140px,#f4dccb 0%,rgba(244,220,203,0) 100%),
      radial-gradient(ellipse 120px 260px at 60px 200px,#d2453a 0%,rgba(210,69,58,0) 100%),
      linear-gradient(160deg,#e9c9a0 0%,#f0d8c2 45%,#e6e3e6 100%);
    -webkit-mask-image:linear-gradient(90deg,#000 55%,transparent 100%);
            mask-image:linear-gradient(90deg,#000 55%,transparent 100%)}
  .brand-mark{position:absolute;right:22px;top:60px;display:flex;align-items:center;gap:12px}
  .brand-mark .dot{width:34px;height:34px;border-radius:50%;background:var(--blue)}
  .brand-mark .name{font-family:"Montserrat",sans-serif;font-weight:600;font-size:22px;
    letter-spacing:2px;color:var(--blue);text-transform:uppercase;line-height:1.25}
  .headline{position:absolute;right:22px;top:212px;text-align:right;font-family:"Montserrat",sans-serif;font-weight:800}
  .headline .owner{display:block;font-size:45px;color:var(--navy);line-height:1}
  .headline .service{display:block;font-size:72px;color:var(--sky);line-height:1;margin-top:4px;letter-spacing:1px}
  .experience{position:absolute;right:22px;top:334px;width:420px;height:34px;border-radius:17px;
    background:var(--navy);color:#fff;font-family:"Montserrat",sans-serif;font-weight:700;
    font-size:22px;display:flex;align-items:center;justify-content:center;letter-spacing:.5px}
  .promise{position:absolute;right:22px;top:386px;text-align:right}
  .promise h2{font-family:"Montserrat",sans-serif;font-weight:800;font-size:48px;color:var(--navy);line-height:1}
  .promise h2 span{color:var(--sky)}
  .promise p{font-size:19px;line-height:26px;margin-top:6px;color:var(--ink)}
  .promise .pledge{font-family:"Montserrat",sans-serif;font-weight:700;font-size:21px;color:var(--blue);margin-top:0}
  .wave{position:absolute;left:0;top:630px;width:950px;height:170px}
  .portrait{position:absolute;left:515px;top:518px;width:410px;height:380px}
  .about{position:absolute;left:28px;top:774px;width:480px;height:121px;border:1px dashed var(--dot-red);
    padding:12px 10px;font-size:19px;line-height:24px;text-align:justify;text-align-last:center;color:var(--ink)}
  .price{position:absolute;top:910px;height:89px;display:flex;align-items:center;font-family:"Montserrat",sans-serif}
  .price .amount{font-weight:800;font-size:70px;line-height:1;letter-spacing:-1px}
  .price .detail{font-weight:600;font-size:22px;line-height:25px;text-align:center}
  .price-single{left:30px;width:508px;padding-left:16px;gap:16px;border-radius:4px;
    background:linear-gradient(180deg,#1d6fa0 0%,var(--navy) 100%);color:#fff;border:1px dashed #9fd0ea}
  .price-double{left:540px;width:378px;padding-left:16px;gap:18px;border:1px dashed var(--dot-red);background:#fff}
  .price-double .amount{color:var(--navy)}
  .price-double .detail{color:var(--blue);font-size:25px;line-height:25px}
  .testimonial{position:absolute;left:12px;top:1019px;width:923px;height:111px;background:var(--navy);
    color:#fff;text-align:center;padding:10px 70px 0}
  .testimonial blockquote{font-size:15px;line-height:20px}
  .testimonial .quote-mark{font-family:"Montserrat",sans-serif;font-weight:800;color:#b9d6e6;font-size:24px;line-height:0;vertical-align:-6px}
  .testimonial cite{display:block;font-style:normal;font-family:"Montserrat",sans-serif;font-weight:700;font-size:19px;margin-top:8px}
  .contact-bar{position:absolute;left:12px;top:1130px;width:923px;height:34px;background:var(--navy-deep);
    border-bottom:3px solid var(--sky);display:flex;align-items:center;justify-content:space-between;padding:0 16px;
    font-family:"Montserrat",sans-serif;font-weight:700;font-size:17px;color:#fff}
  .contact-bar span{display:flex;align-items:center;gap:7px}
  .contact-bar svg{width:17px;height:17px}
  .follow{position:absolute;left:0;top:1174px;width:950px;text-align:center;font-size:14px;
    display:flex;justify-content:center;align-items:center;gap:6px;color:var(--ink)}
  .follow .dot{width:14px;height:14px;border-radius:50%;background:var(--navy)}
</style>
</head>
<body>
<main class="flyer">
  <div class="hero-photo" role="img" aria-label="Photo of young children leaning over a desk with coloured pencils"></div>

  <div class="brand-mark">
    <span class="dot"></span>
    <span class="name">Marisol Penhaw<br>Tutoring</span>
  </div>

  <h1 class="headline">
    <span class="owner">MARISOL PENHAW</span>
    <span class="service">TUTORING</span>
  </h1>

  <div class="experience">OVER 25 YEARS EXPERIENCE</div>

  <section class="promise">
    <h2>IT CAN <span>HAPPEN</span></h2>
    <p>I am a teacher, I am a father,<br>I am a lifelong learner and</p>
    <p class="pledge">I CAN HELP YOUR CHILD IMPROVE</p>
  </section>

  <svg class="wave" viewBox="0 0 950 170" aria-hidden="true">
    <path d="M0,40 C150,90 300,90 420,55 C480,38 540,30 600,36 L600,52 C520,48 430,82 300,98 C170,112 70,82 0,62Z" fill="var(--sky)"/>
    <path d="M0,72 C150,122 300,132 420,96 C480,78 540,66 600,70 L600,104 C500,108 390,160 250,156 C150,152 60,124 0,108Z" fill="var(--navy)"/>
  </svg>

  <svg class="portrait" viewBox="0 0 410 380">
    <path d="M330,60 C370,40 400,30 410,30 L410,120 C395,110 370,100 345,98Z" fill="var(--navy)"/>
    <path d="M330,40 C370,22 400,14 410,14 L410,28 C395,30 370,40 340,55Z" fill="var(--sky)"/>
    <circle cx="205" cy="190" r="188" fill="var(--navy)"/>
    <circle cx="205" cy="190" r="170" fill="#ffffff"/>
    <circle cx="205" cy="190" r="162" fill="#b9bec4"/>
    <defs>
      <linearGradient id="portraitTone" x1="0" y1="0" x2="0" y2="1">
        <stop offset="0" stop-color="#b98a6a"/>
        <stop offset="0.5" stop-color="#d9b39a"/>
        <stop offset="1" stop-color="#b7d0dc"/>
      </linearGradient>
    </defs>
    <circle cx="205" cy="190" r="154" fill="url(#portraitTone)" role="img" aria-label="Portrait photo of the tutor smiling in front of a bookshelf"/>
  </svg>

  <p class="about">I tutor children from K-9 in English and Maths. I'm mainly aiming at parents whose children are struggling a little bit at school although I can help children who are doing well too.</p>

  <div class="price price-single">
    <span class="amount">$45</span>
    <span class="detail">for sessions of<br>an hour and 15 minutes.</span>
  </div>
  <div class="price price-double">
    <span class="amount">$80</span>
    <span class="detail">2 sessions<br>per week</span>
  </div>

  <section class="testimonial">
    <blockquote><span class="quote-mark">“</span> Our son has been tutored by Marisol now for the past 2 years - we have noticed a big improvement with his spelling and mathematics. This has also helped our son's confidence in his daily schooling and he now has started to enjoy school again . Thanks Marisol <span class="quote-mark">”</span></blockquote>
    <cite>- Dorian and Pella Varnes</cite>
  </section>

  <div class="contact-bar">
    <span><svg viewBox="0 0 24 24"><circle cx="12" cy="12" r="11" fill="#fff"/><path d="M8 6l2 0 1 3-1.5 1.2a8 8 0 0 0 4.3 4.3L15 13l3 1v2a2 2 0 0 1-2 2A10 10 0 0 1 6 8a2 2 0 0 1 2-2z" fill="var(--navy-deep)"/></svg>0400 555 019</span>
    <span><svg viewBox="0 0 24 24"><circle cx="12" cy="12" r="11" fill="#fff"/><rect x="6" y="8" width="12" height="8" rx="1" fill="var(--navy-deep)"/><path d="M6.5 8.5L12 13l5.5-4.5" stroke="#fff" stroke-width="1.2" fill="none"/></svg>MARISOLPENHAW@MAIL.EXAMPLE</span>
    <span><svg viewBox="0 0 24 24"><circle cx="12" cy="12" r="10" fill="none" stroke="#fff" stroke-width="2"/><ellipse cx="12" cy="12" rx="4" ry="10" fill="none" stroke="#fff" stroke-width="1.5"/><path d="M2 12h20" stroke="#fff" stroke-width="1.5"/></svg>WWW.MARISOLPENHAW.EXAMPLE</span>
  </div>

  <p class="follow">Follow at : <span class="dot"></span> marisolpenhawtutoring</p>
</main>
</body>
</html>
```